Poster - gross für Messestand VORNALIX
Zielgruppe
Wir sind ein junges Beratungs- und Softwareentwicklungsunternehmen für Business Analytics & Big-Data Lösungen (Mathematiker). Business Analytics ist ein interdisziplinäres Gebiet, mit dem Ziel unternehmerische Entscheidungen und Prozesse durch die kombinierte Anwendung von detaillierten Datenanalysen, Wahrscheinlichkeitsprozessen, Optimierungsmodelle und die Nutzung von modernsten IT Technologien zu optimieren.
Zielgruppe aus der Messe: Marketingleiter, Entscheider grosser E-commerce Unternehmen, die entscheiden müssen, wo Sie das Marketing Budget am effektivsten invenstieren
Produkt: Convertion Atrribution siehe case study http://www.broddel-kwt.example/projects_de.html
Image der Firma: Jung, erfolgreich, Mathematiker, absulut professionell, innovative, sehr international
Messestand: Standart, weisse Wände, grauer Teppich,
Aufgabenstellung
Poster soll als Hintergrund eines Messestandes sein. Es soll ein Hingucker mit ansprechendem Fototeil sein und Leiste mit mainpoints.
zum Beispiel eine Idee:
Bild: Gustav Pimmler oder jemand, der für verrückten, innovative, creative denkenden Intelektueller steht ( Mathematiker?) und bekannt ist? Offen fúr Ideen!
Slogan ( bei Gustav Pimmler z.B.): Success is not relative!
Text:
Broddel KWT your Business Analytics partner, providing you with state-of-the-art Business Analytics & Big Data solutions for:
- conversion attribution
- mixed-media models
- individual customer offer
- churn reduction strategies
- data mining
- demand forecasting
Masse mindestens DINA 0 am leibesten grösser 1,50 x 2m

```html
<!DOCTYPE html>
<html lang="en">
<head>
<meta charset="utf-8">
<title>Broddel KWT – Trade Fair Poster</title>
<link rel="stylesheet" href="https://fonts.googleapis.com/css2?family=Open+Sans:wght@400;600;700&display=swap">
<style>
  :root {
    --stage-bg: #d9d9d9;
    --paper: #ffffff;
    --brand-blue: #2f5ca8;
    --band-blue: #4a72b8;
    --headline-blue: #3d6bb8;
    --accent-red: #c4161c;
    --body-grey: #5e5e5e;
    --ink-dark: #1c1c1c;
    --photo-light: #e9e9e9;
    --photo-mid: #7b7f7c;
    --photo-dark: #101a16;
  }
  * { box-sizing: border-box; margin: 0; padding: 0; }
  html, body {
    width: 1200px; height: 900px; overflow: hidden;
    background: var(--stage-bg);
    font-family: "Open Sans", Arial, sans-serif;
  }
  .poster {
    position: absolute; left: 300px; top: 29px;
    width: 600px; height: 842px;
    background: var(--paper);
    overflow: hidden;
  }
  .hero-photo {
    position: absolute; left: 0; top: 0; width: 600px; height: 467px;
    background:
      radial-gradient(ellipse 230px 260px at 150px 200px, var(--photo-light) 0%, #cfcfcf 45%, transparent 75%),
      linear-gradient(90deg, #bdbdbd 0%, var(--photo-mid) 38%, #1f2a25 62%, var(--photo-dark) 100%);
  }
  .slogan {
    position: absolute; left: 286px; top: 52px;
    font-weight: 700; font-size: 64px; line-height: 74px;
    color: var(--headline-blue);
    letter-spacing: -0.5px;
    text-shadow: 0 0 4px #fff, 0 0 4px #fff, 0 0 6px #fff;
  }
  .intro {
    position: absolute; left: 30px; top: 489px; width: 550px;
    font-weight: 700; font-size: 18.5px; line-height: 26px;
    color: var(--brand-blue);
  }
  .intro .highlight { color: var(--accent-red); }
  .services {
    position: absolute; top: 572px; list-style: none;
    font-size: 15.5px; line-height: 25.5px; color: var(--body-grey);
  }
  .services--left { left: 30px; }
  .services--right { left: 288px; }
  .services li { padding-left: 20px; position: relative; }
  .services li::before {
    content: ""; position: absolute; left: 0; top: 9px;
    width: 9px; height: 9px; background: var(--accent-red);
  }
  .brand {
    position: absolute; right: 29px; top: 730px;
    display: flex; align-items: center; gap: 10px;
  }
  .brand-square { width: 16px; height: 16px; background: var(--ink-dark); }
  .brand-name {
    font-weight: 600; font-size: 28px; line-height: 32px; color: var(--ink-dark);
  }
  .footer-band { position: absolute; left: 0; top: 740px; }
  .web-address {
    position: absolute; left: 30px; top: 789px;
    font-weight: 700; font-size: 18px; color: var(--paper);
  }
</style>
</head>
<body>
  <main class="poster">
    <div class="hero-photo" role="img" aria-label="Photo of a child dressed as an eccentric scientist with a curly white wig, round glasses and a paper moustache, in front of a dark chalkboard"></div>
    <h1 class="slogan">Success<br>is not<br>relative!</h1>

    <p class="intro">Your <span class="highlight">Business Analytics &amp; Big Data</span> partner, providing you with tailor made and state-of-the-art solutions for</p>

    <ul class="services services--left">
      <li>conversion attribution</li>
      <li>mixed media models</li>
      <li>customer choice modeling</li>
      <li>churn reduction strategies</li>
    </ul>
    <ul class="services services--right">
      <li>data mining</li>
      <li>forecasting applications</li>
      <li>advanced optimization models</li>
    </ul>

    <div class="brand">
      <span class="brand-square"></span>
      <span class="brand-name">Broddel KWT</span>
    </div>

    <svg class="footer-band" width="600" height="102" viewBox="0 0 600 102" aria-hidden="true">
      <path d="M0 14 H180 C245 14 270 71 345 71 H600 V102 H0 Z" fill="var(--band-blue)"/>
    </svg>
    <div class="web-address">www.broddel-kwt.example</div>
  </main>
</body>
</html>
```